Business card design for Automotive workshop

We need a business card for a new automotive repair and tyre shop called Keelstone Prime Automotive located in New Zealand. We are a clean, modern and fresh workshop and company.

Front needs to feature logo,
my name:
Marlo Fitzgerald (director)

Address:
42 Tamsin Road
Whitianga 3510

Phone: 07 541 2298
Mobile: 027 419 5073
Email: office@keelstoneautomotive.co.nz
Website: keelstoneautomotive.co.nz

Back needs to feature an area to write down appointment details, date and time.

Also feature a list of jobs and work we do such as,
Vehicle Servicing
All Mechanical Repairs
Warrant of Fitness
Tyres & Wheel Alignments
Automotive Diagnostics
Automotive Parts & Supplies

```html
<!DOCTYPE html>
<html lang="en">
<head>
<meta charset="utf-8">
<title>Keelstone Prime Automotive – Business Card</title>
<link href="https://fonts.googleapis.com/css2?family=Roboto:wght@400;500;700;900&display=swap" rel="stylesheet">
<style>
  :root {
    --bg: #2b2d30;
    --card: #0b0b0c;
    --red: #e3232c;
    --white: #ffffff;
    --grey: #bdbdbd;
  }
  * { box-sizing: border-box; margin: 0; padding: 0; }
  html, body { width: 1200px; height: 900px; overflow: hidden; }
  body {
    background: var(--bg);
    font-family: "Roboto", Arial, sans-serif;
    color: var(--white);
    position: relative;
  }
  .card {
    position: absolute;
    left: 250px;
    width: 700px;
    height: 400px;
    background: var(--card);
    overflow: hidden;
    box-shadow: 0 12px 30px rgba(0,0,0,.45);
  }
  .card--front { top: 30px; }
  .card--back { top: 470px; }

  /* Front */
  .brand {
    position: absolute;
    top: 50px; right: 50px;
    display: flex; align-items: center; gap: 14px;
  }
  .brand__mark { width: 22px; height: 22px; background: var(--red); }
  .brand__name {
    font-weight: 900;
    font-size: 40px;
    letter-spacing: 2px;
    color: var(--red);
    text-transform: uppercase;
    line-height: 1.05;
    text-align: right;
  }
  .person {
    position: absolute;
    top: 175px; right: 50px;
    text-align: right;
  }
  .person__name {
    color: var(--red);
    font-size: 30px;
    font-weight: 500;
    letter-spacing: 1px;
    text-transform: uppercase;
  }
  .person__role {
    font-size: 17px;
    letter-spacing: 2px;
    text-transform: uppercase;
    margin-top: 4px;
  }
  .contacts {
    position: absolute;
    top: 250px; left: 40px; right: 40px;
    display: flex; justify-content: space-between;
    font-size: 17px;
  }
  .contacts__col { display: flex; flex-direction: column; gap: 10px; }
  .contact { display: flex; align-items: center; gap: 10px; }
  .contact svg { width: 18px; height: 18px; flex: none; }
  .address-band {
    position: absolute;
    left: 0; right: 0; bottom: 0;
    height: 68px;
    background: var(--red);
    display: flex; align-items: center;
    padding-left: 40px;
    font-size: 22px;
    font-weight: 500;
  }

  /* Back */
  .appointment__title {
    position: absolute;
    top: 34px; left: 0; right: 0;
    display: flex; justify-content: center; align-items: center; gap: 16px;
    font-size: 30px; font-weight: 900; letter-spacing: 7px;
  }
  .appointment__title svg { width: 46px; height: 14px; }
  .appointment__band {
    position: absolute;
    top: 100px; left: 0; right: 0;
    height: 70px;
    background: var(--white);
    color: var(--card);
    display: flex; align-items: center; gap: 40px;
    padding: 0 40px;
    font-weight: 900; font-size: 20px; letter-spacing: 3px;
  }
  .field { display: flex; align-items: flex-end; gap: 12px; flex: 1; }
  .field__line { flex: 1; border-bottom: 1.5px solid var(--card); height: 18px; }
  .services {
    position: absolute;
    top: 205px; left: 40px; right: 40px;
    display: flex; justify-content: space-between;
  }
  .services__list { list-style: none; display: flex; flex-direction: column; gap: 14px; font-size: 20px; }
  .services__item { display: flex; align-items: center; gap: 12px; }
  .services__item svg { width: 20px; height: 20px; flex: none; }
</style>
</head>
<body>

<section class="card card--front">
  <div class="brand">
    <span class="brand__mark"></span>
    <div class="brand__name">Keelstone Prime<br>Automotive</div>
  </div>

  <div class="person">
    <div class="person__name">Marlo Fitzgerald</div>
    <div class="person__role">Director</div>
  </div>

  <div class="contacts">
    <div class="contacts__col">
      <div class="contact">
        <svg viewBox="0 0 24 24" aria-hidden="true"><path fill="#e3232c" d="M6.6 10.8a15 15 0 0 0 6.6 6.6l2.2-2.2c.3-.3.7-.4 1-.2 1.1.4 2.3.6 3.6.6.6 0 1 .4 1 1V20c0 .6-.4 1-1 1A17 17 0 0 1 3 4c0-.6.4-1 1-1h3.5c.6 0 1 .4 1 1 0 1.3.2 2.5.6 3.6.1.3 0 .7-.2 1z"/></svg>
        <span>07 541 2298</span>
      </div>
      <div class="contact">
        <svg viewBox="0 0 24 24" aria-hidden="true"><rect x="6" y="2" width="12" height="20" rx="2" fill="none" stroke="#e3232c" stroke-width="2"/><circle cx="12" cy="18" r="1.2" fill="#e3232c"/></svg>
        <span>027 419 5073</span>
      </div>
    </div>
    <div class="contacts__col">
      <div class="contact">
        <svg viewBox="0 0 24 24" aria-hidden="true"><rect x="2" y="5" width="20" height="14" rx="1.5" fill="#e3232c"/><path d="M3 6l9 7 9-7" fill="none" stroke="#0b0b0c" stroke-width="1.6"/></svg>
        <span>office@keelstoneautomotive.co.nz</span>
      </div>
      <div class="contact">
        <svg viewBox="0 0 24 24" aria-hidden="true"><g fill="none" stroke="#e3232c" stroke-width="1.8"><circle cx="12" cy="12" r="9.5"/><ellipse cx="12" cy="12" rx="4.2" ry="9.5"/><path d="M2.5 12h19M4 7h16M4 17h16"/></g></svg>
        <span>www.keelstoneautomotive.co.nz</span>
      </div>
    </div>
  </div>

  <div class="address-band">42 Tamsin Road, Whitianga 3510</div>
</section>

<section class="card card--back">
  <h2 class="appointment__title">
    <svg viewBox="0 0 46 14" aria-hidden="true"><path d="M0 2h46M8 12h38" stroke="#fff" stroke-width="3"/></svg>
    APPOINTMENT
    <svg viewBox="0 0 46 14" aria-hidden="true"><path d="M0 2h46M0 12h38" stroke="#fff" stroke-width="3"/></svg>
  </h2>

  <div class="appointment__band">
    <div class="field"><span>DATE</span><span class="field__line"></span></div>
    <div class="field"><span>TIME</span><span class="field__line"></span></div>
  </div>

  <div class="services">
    <ul class="services__list">
      <li class="services__item"><svg viewBox="0 0 20 20" aria-hidden="true"><circle cx="10" cy="10" r="10" fill="#fff"/><path d="M5.5 10.5l3 3 6-6.5" fill="none" stroke="#0b0b0c" stroke-width="2.2"/></svg>Vehicle Servicing</li>
      <li class="services__item"><svg viewBox="0 0 20 20" aria-hidden="true"><circle cx="10" cy="10" r="10" fill="#fff"/><path d="M5.5 10.5l3 3 6-6.5" fill="none" stroke="#0b0b0c" stroke-width="2.2"/></svg>All Mechanical Repairs</li>
      <li class="services__item"><svg viewBox="0 0 20 20" aria-hidden="true"><circle cx="10" cy="10" r="10" fill="#fff"/><path d="M5.5 10.5l3 3 6-6.5" fill="none" stroke="#0b0b0c" stroke-width="2.2"/></svg>Warrant of Fitness</li>
    </ul>
    <ul class="services__list">
      <li class="services__item"><svg viewBox="0 0 20 20" aria-hidden="true"><circle cx="10" cy="10" r="10" fill="#fff"/><path d="M5.5 10.5l3 3 6-6.5" fill="none" stroke="#0b0b0c" stroke-width="2.2"/></svg>Tyres &amp; Wheel Alignments</li>
      <li class="services__item"><svg viewBox="0 0 20 20" aria-hidden="true"><circle cx="10" cy="10" r="10" fill="#fff"/><path d="M5.5 10.5l3 3 6-6.5" fill="none" stroke="#0b0b0c" stroke-width="2.2"/></svg>Automotive Diagnostics</li>
      <li class="services__item"><svg viewBox="0 0 20 20" aria-hidden="true"><circle cx="10" cy="10" r="10" fill="#fff"/><path d="M5.5 10.5l3 3 6-6.5" fill="none" stroke="#0b0b0c" stroke-width="2.2"/></svg>Automotive Parts &amp; Supplies</li>
    </ul>
  </div>
</section>

</body>
</html>
```